Revamping and duplicating of existing business card

We are a painting and decorating business based in London and need a couple of business cards made up for the following people.

1. Maribel Osgood
2. Tobias Penrick

Measurements - 85 X 55 mm
Font: Blue highway
Colour: No idea! Would be great to have a pantone for the pink if possible?

I’ve attached all the logos and old artwork etc.
Here are the amendments I would definitely like...

1. Maribel

format mobile number correctly: 07512 368 904

Add title: Decorator
Use: Osgood Decorating Logo
Add twitter logo & @osgooddecor
Add tradevouch logo
Add HFG Logo
Make it all look beautiful/revamp/tweak - whatever you think…

2. Tobias

Decorator

07643 295 581
tobias@osgooddecorating.co.uk
Updates

Hello! Thanks so much for all your designs. This is such a great way to get these things done... Just to clarify, Please do not alter our logo at all. The 'splat' appears on our van, tshirts, quotes etc and is very much part of our branding. Colour scheme: Pink, black and white. Thanks Maribel

Project Deadline Extended
Reason: Not 100% sold on any of the designs so far but very grateful for all the submissions. Keep it simple and quirky please. Thanks Maribel

Industry/Entity Type

Painting

Requirements
Must have
• Pink & Black Colour scheme
Osgood Decorating Logo
Blue Highway font

```html
<!DOCTYPE html>
<html lang="en">
<head>
<meta charset="utf-8">
<title>Osgood Decorating – Tobias Penrick business card</title>
<link rel="stylesheet" href="https://fonts.googleapis.com/css2?family=Ubuntu:wght@400;500;700&display=swap">
<style>
  :root {
    --backdrop: #e6e4e7;
    --card: #ffffff;
    --splat-pink: #c2187a;
    --ink: #111111;
    --muted: #555555;
    --badge-navy: #2b3475;
    --badge-red: #c8102e;
    --social-blue: #4fb3dd;
  }
  * { margin: 0; padding: 0; box-sizing: border-box; }
  html, body {
    width: 1200px; height: 960px; overflow: hidden;
    background: var(--backdrop);
    font-family: "Ubuntu", sans-serif;
    color: var(--ink);
  }
  .card {
    position: absolute; left: 100px; top: 156px;
    width: 1000px; height: 647px;
    background: var(--card);
    box-shadow: 0 10px 30px rgba(0,0,0,.18);
    overflow: hidden;
  }
  .splat-area {
    position: absolute; left: 0; top: 0;
    width: 450px; height: 500px;
    background: linear-gradient(160deg, #d0258a 0%, var(--splat-pink) 55%, #a8146a 100%);
  }
  .brand {
    position: absolute; left: 56px; top: 300px;
    font-weight: 700; font-size: 62px; line-height: 1;
    color: var(--ink);
    letter-spacing: 1px;
  }
  .person {
    position: absolute; right: 70px; top: 90px; text-align: right;
  }
  .person__name { font-size: 46px; font-weight: 500; }
  .person__role { font-size: 28px; font-weight: 500; margin-top: 4px; }
  .contact {
    position: absolute; right: 70px; top: 250px; text-align: right;
  }
  .contact__phone { font-size: 46px; font-weight: 500; }
  .contact__email { font-size: 27px; font-weight: 500; margin-top: 26px; }
  .membership {
    position: absolute; right: 70px; top: 430px; text-align: left;
  }
  .membership__intro { font-size: 12px; color: var(--muted); }
  .membership__name {
    display: flex; align-items: center; gap: 10px;
    font-size: 36px; font-weight: 500; color: var(--ink);
  }
  .membership__mark { width: 16px; height: 16px; background: var(--badge-red); }
  .association-badge {
    position: absolute; left: 590px; top: 490px;
  }
  .social {
    position: absolute; left: 40px; bottom: 36px;
    display: flex; align-items: center; gap: 16px;
    font-size: 30px; font-weight: 700;
  }
  .social__icon {
    width: 52px; height: 52px; border-radius: 6px; background: var(--social-blue);
  }
</style>
</head>
<body>
  <article class="card">
    <div class="splat-area" role="img" aria-label="Pink paint splat brand mark"></div>
    <div class="brand">Osgood<br>Decorating</div>

    <div class="person">
      <p class="person__name">Tobias Penrick</p>
      <p class="person__role">Decorator</p>
    </div>

    <div class="contact">
      <p class="contact__phone">07643 295 581</p>
      <p class="contact__email">tobias@osgooddecorating.co.uk</p>
    </div>

    <div class="membership">
      <p class="membership__intro">Proud members of</p>
      <p class="membership__name"><span class="membership__mark"></span>tradevouch</p>
    </div>

    <svg class="association-badge" width="90" height="90" viewBox="0 0 90 90" role="img" aria-label="HFG member badge">
      <circle cx="45" cy="45" r="40" fill="#ffffff" stroke="var(--badge-navy)" stroke-width="8"/>
    </svg>

    <div class="social">
      <span class="social__icon"></span>
      <span class="social__handle">@osgooddecor</span>
    </div>
  </article>
</body>
</html>
```